Company Mission & Values Poster

I'd like an A2 Portrait Poster displaying our company's Mission & Values.
See our website for our logo, fonts, mission & values.
https://talvendo.com.au/

Our Mission: Creating homes for abundant life
Values: Love, Thinking, Team, Zoe.

Some ideas to consider:
Mission as the Headline then
A logo for each of the 4 Values and the words

Target Market(s)

Myself & my team

Industry/Entity Type

Real Estate

Font styles to use
Other font styles liked:
• Company fonts as seen on our website

```html
<!DOCTYPE html>
<html lang="en">
<head>
<meta charset="utf-8">
<title>Talvendo Mission &amp; Values Poster</title>
<link rel="stylesheet" href="https://fonts.googleapis.com/css2?family=Bebas+Neue&family=Josefin+Sans:wght@300;400&family=Playfair+Display:ital,wght@0,500;1,500&family=Forum&display=swap">
<style>
  :root {
    --poster-green: #0f3f30;
    --ink-light: #f4f3ee;
  }
  * { margin: 0; padding: 0; box-sizing: border-box; }
  html, body {
    width: 914px;
    height: 1200px;
    overflow: hidden;
    background: var(--poster-green);
  }
  .poster {
    position: relative;
    width: 914px;
    height: 1200px;
    background: var(--poster-green);
    color: var(--ink-light);
    text-align: center;
  }
  .mission {
    position: absolute;
    top: 108px;
    left: 0;
    width: 100%;
    font-family: "Josefin Sans", sans-serif;
    font-weight: 400;
    font-size: 41px;
    line-height: 62px;
  }
  .mission em {
    font-family: "Playfair Display", serif;
    font-style: italic;
    font-weight: 500;
    font-size: 44px;
  }
  .values {
    position: absolute;
    top: 290px;
    left: 0;
    width: 100%;
    list-style: none;
  }
  .value {
    display: block;
  }
  .value--bold {
    font-family: "Bebas Neue", sans-serif;
    font-size: 150px;
    line-height: 118px;
    letter-spacing: 1px;
  }
  .value--light {
    font-family: "Josefin Sans", sans-serif;
    font-weight: 300;
    font-size: 162px;
    line-height: 136px;
  }
  .value--serif {
    font-family: "Forum", serif;
    font-size: 176px;
    line-height: 120px;
    letter-spacing: 4px;
  }
  .brand {
    position: absolute;
    top: 968px;
    left: 0;
    width: 100%;
    display: flex;
    justify-content: center;
    align-items: center;
    gap: 12px;
  }
  .brand-dot {
    width: 22px;
    height: 22px;
    border-radius: 50%;
    background: var(--ink-light);
  }
  .brand-name {
    font-family: "Playfair Display", serif;
    font-weight: 500;
    font-size: 38px;
    letter-spacing: 4px;
    color: var(--ink-light);
  }
</style>
</head>
<body>
  <main class="poster">
    <h1 class="mission">Creating Homes<br>for <em>Abundant Life</em></h1>
    <ul class="values">
      <li class="value value--bold">LOVE</li>
      <li class="value value--light">team</li>
      <li class="value value--bold">THINKING</li>
      <li class="value value--serif">zoe</li>
    </ul>
    <footer class="brand">
      <span class="brand-dot"></span>
      <span class="brand-name">TALVENDO</span>
    </footer>
  </main>
</body>
</html>
```